Brisk Hollow Builders Needs A Flyer

We need a flyer for our newest product "The Cedarlane Garden Workroom"

Here is some copy for the flyer:

1. More and more people everyday are working from home and finding it difficult to disconnect from home activities in order to focus on their work. They are also finding it very expensive to add on to their existing house for a quiet place. Our archatectually stunning, Cedarlane Garden Workroom is the answer. The office studio measures 16' wide and 10' deep. 160 Square feet of space.

Perfect for dozens of purposes. Home office, design studio, artist studio, home school office, reading room, craft studio, drafting room.

Features include:

- Steel Framing. 40-60% lighter then wood, higher strength to weight ratio, resistant to mold and fire and steel is the most recycled material on earth!
- Spray foam insulation. Cool in the summer and warm in the winter.
- HVAC Mini Split with wireless remote control and thermostat.
- 100% Off grid with enough solar and battery storage to run your entire office. No need to pay for an expensive electric installation.
- Flush fitting floor outlets to reduce wires.
- TV mount (Optional with pre-wired electric, HDMI, digital audio & Cat 6)
- Windows are tempered glass custom made by Morvik Glazing.
- Solar qualifies for a 26% tax credit. This is not a write-off rather it is a direct reduction on your tax obligation.
- Thousands of dollars less than adding onto your home.
- Custom color, siding, features available.

This beautiful back yard office is delivered 100% assembled and ready to enjoy on the day of delivery.

We ship nationwide from our factory in South Carolina. Give us a call anytime to speak to a designer and start your dream office today!

555-318-4027
info@BriskHollowBuilders.example

```html
<!DOCTYPE html>
<html lang="en">
<head>
<meta charset="utf-8">
<title>The Cedarlane Garden Workroom — Brisk Hollow Builders</title>
<link href="https://fonts.googleapis.com/css2?family=Montserrat:wght@400;500;600;700&family=Open+Sans:wght@400;600;700&display=swap" rel="stylesheet">
<style>
  :root {
    --green: #3f9d4a;
    --charcoal: #4b4743;
    --footer: #55514d;
    --beige: #ddd3c5;
    --thumb: #d9cfc1;
    --ink: #1d1d1b;
    --text: #3a3a3a;
    --paper: #ffffff;
  }
  * { margin: 0; padding: 0; box-sizing: border-box; }
  html, body { width: 861px; height: 1200px; overflow: hidden; background: var(--paper); }
  .flyer { position: relative; width: 861px; height: 1200px; background: var(--paper); font-family: "Open Sans", Arial, sans-serif; color: var(--text); }

  .brand { position: absolute; left: 28px; top: 40px; width: 240px; display: flex; align-items: center; gap: 10px; }
  .brand-dot { width: 30px; height: 30px; border-radius: 50%; background: var(--green); flex: none; }
  .brand-name { font-family: "Montserrat", Arial, sans-serif; font-weight: 700; font-size: 21px; line-height: 1.1; color: var(--green); }

  .headline { position: absolute; left: 300px; top: 28px; width: 545px; white-space: nowrap; font-family: "Montserrat", Arial, sans-serif; font-weight: 600; font-size: 40px; line-height: 1.2; letter-spacing: 1px; color: var(--ink); text-transform: uppercase; }

  .accent-top { position: absolute; left: 555px; top: 143px; width: 270px; height: 22px; background: var(--green); }
  .accent-left { position: absolute; left: 0; top: 138px; width: 40px; height: 18px; background: var(--green); }
  .accent-photo { position: absolute; left: 40px; top: 340px; width: 42px; height: 26px; background: var(--green); }

  .hero-photo { position: absolute; left: 40px; top: 143px; width: 785px; height: 520px;
    background: linear-gradient(180deg, #c9d8e6 0%, #b9c6b3 30%, #6e7a62 58%, #4f5a45 78%, #8f8d85 100%); }

  .thumb { position: absolute; z-index: 2; left: 579px; width: 210px; background: var(--thumb); border: 7px solid #fff; box-shadow: 0 2px 6px rgba(0,0,0,.25); }
  .thumb-frame { top: 216px; height: 170px; }
  .thumb-front { top: 408px; height: 160px; }
  .thumb-side { top: 586px; height: 150px; }

  .intro { position: absolute; left: 40px; top: 662px; width: 785px; height: 144px; background: var(--charcoal); padding: 8px 262px 0 28px; color: #ece9e4; font-size: 13px; line-height: 17px; text-align: justify; }
  .intro p + p { margin-top: 10px; }

  .features-bar { position: absolute; left: 40px; top: 812px; width: 785px; height: 28px; background: var(--green); color: #fff; font-family: "Montserrat", Arial, sans-serif; font-weight: 700; font-size: 15px; line-height: 28px; padding-left: 22px; letter-spacing: .5px; }

  .features { position: absolute; left: 40px; top: 848px; width: 785px; display: grid; grid-template-columns: 1fr 1fr 1fr; column-gap: 12px; }
  .features ul { list-style: none; }
  .features li { position: relative; padding-left: 14px; font-size: 11.6px; line-height: 1.5; margin-bottom: 8px; color: var(--text); }
  .features li::before { content: ""; position: absolute; left: 0; top: 5px; width: 7px; height: 7px; border: 1.5px solid #9a9a9a; border-radius: 50%; }
  .col-2, .col-3 { border-left: 1px dotted #b8b8b8; padding-left: 12px; }

  .delivery { position: absolute; left: 40px; top: 1046px; width: 785px; height: 82px; background: var(--beige); padding: 12px 18px; font-weight: 700; font-size: 12.6px; line-height: 1.5; color: #3b3633; }
  .delivery p + p { margin-top: 8px; }

  .contact-bar { position: absolute; left: 40px; top: 1134px; width: 785px; height: 32px; background: var(--footer); color: #fff; display: flex; justify-content: space-between; align-items: center; padding: 0 18px; font-size: 13px; }
  .contact-item { display: flex; align-items: center; gap: 8px; }
  .contact-item svg { width: 14px; height: 14px; fill: #fff; }
</style>
</head>
<body>
<main class="flyer">
  <div class="accent-left"></div>
  <div class="brand">
    <span class="brand-dot"></span>
    <span class="brand-name">Brisk Hollow Builders</span>
  </div>
  <h1 class="headline">The Cedarlane<br>Garden Workroom</h1>

  <div class="hero-photo" role="img" aria-label="Photo of a dark-framed garden office with glass walls and a wooden door, set among trees and shrubs"></div>
  <div class="accent-top"></div>
  <div class="accent-photo"></div>

  <section class="intro">
    <p>More and more people everyday are working from home and finding it difficult to disconnect from home activities in order to focus on their work. They are also finding it very expensive to add on to their existing house for a quiet place. Our archatectually stunning, Cedarlane Garden Workroom is the answer. The office studio measures 16' wide and 10' deep. 160 square feet of space.</p>
    <p>Perfect for dozens of purposes. Home office, design studio, artist studio, home school office, reading room, craft studio, drafting room.</p>
  </section>

  <div class="thumb thumb-frame" role="img" aria-label="Exploded drawing of the workroom's steel frame and panels"></div>
  <div class="thumb thumb-front" role="img" aria-label="Rendering of the workroom front elevation"></div>
  <div class="thumb thumb-side" role="img" aria-label="Rendering of the workroom seen from an angle"></div>

  <h2 class="features-bar">KEY FEATURES:</h2>
  <section class="features">
    <ul class="col-1">
      <li>Steel Framing. 40-60% lighter then wood, higher strength to weight ratio, resistant to mold and fire and steel is the most recycled material on earth</li>
      <li>Spray foam insulation. Cool in the summer and warm in the winter</li>
      <li>HVAC Mini Split with wireless remote control and thermostat</li>
    </ul>
    <ul class="col-2">
      <li>100% Off grid with enough solar and battery storage to run your entire office. No need to pay for an expensive electric installation</li>
      <li>Flush fitting floor outlets to reduce wires</li>
      <li>TV mount (Optional with pre-wired electric, HDMI, Digital audio &amp; Cat 6)</li>
    </ul>
    <ul class="col-3">
      <li>Windows are tempered glass custom made by Morvik Glazing</li>
      <li>Solar qualifies for a 26% tax credit. This is not a write-off rather it is a direct reduction on your tax obligation</li>
      <li>Thousands of dollars less than adding onto your home</li>
      <li>Custom color, siding, features available</li>
    </ul>
  </section>

  <section class="delivery">
    <p>This beautiful back yard office is delivered 100% assembled and ready to enjoy on the day of delivery.</p>
    <p>We ship nationwide from our factory in South Carolina. Give us a call anytime to speak to a designer and start your dream office today!</p>
  </section>

  <footer class="contact-bar">
    <span class="contact-item">
      <svg viewBox="0 0 24 24" aria-hidden="true"><path d="M6.6 10.8a15.1 15.1 0 0 0 6.6 6.6l2.2-2.2a1 1 0 0 1 1-.25 11.4 11.4 0 0 0 3.6.57 1 1 0 0 1 1 1V20a1 1 0 0 1-1 1A17 17 0 0 1 3 4a1 1 0 0 1 1-1h3.5a1 1 0 0 1 1 1c0 1.25.2 2.450.57 3.57a1 1 0 0 1-.25 1z"/></svg>
      555 318 4027
    </span>
    <span class="contact-item">
      <svg viewBox="0 0 24 24" aria-hidden="true"><path d="M12 2a10 10 0 1 0 0 20 10 10 0 0 0 0-20zm6.9 6h-3a15.6 15.6 0 0 0-1.4-3.6A8 8 0 0 1 18.9 8zM12 4c.8 1.2 1.5 2.5 1.9 4h-3.8c.4-1.5 1.1-2.8 1.9-4zM4.3 14a8 8 0 0 1 0-4h3.4a16 16 0 0 0 0 4zm.8 2h3a15.6 15.6 0 0 0 1.4 3.6A8 8 0 0 1 5.1 16zm3-8h-3a8 8 0 0 1 4.4-3.6A15.6 15.6 0 0 0 8.1 8zM12 20c-.8-1.2-1.5-2.5-1.9-4h3.8c-.4 1.5-1.1 2.8-1.9 4zm2.3-6H9.7a14.7 14.7 0 0 1 0-4h4.6a14.7 14.7 0 0 1 0 4zm.2 5.6a15.6 15.6 0 0 0 1.4-3.6h3a8 8 0 0 1-4.4 3.6zm1.8-5.6a16 16 0 0 0 0-4h3.4a8 8 0 0 1 0 4z"/></svg>
      info@BriskHollowBuilders.example
    </span>
  </footer>
</main>
</body>
</html>
```